Step and Repeat Backdrop for wedding reception photo booth

Would like to have a Step and Repeat Backdrop (8 foot high by 10 foot wide) that incorporates the wedding logo (attached) and the names Clara and Bruno. Background should be white, and wedding colors are burgundy and gold. Show me creativity :-) I have included some random samples.

```html
<!DOCTYPE html>
<html lang="en">
<head>
<meta charset="utf-8">
<title>Clara &amp; Bruno – Step and Repeat Backdrop</title>
<link rel="stylesheet" href="https://fonts.googleapis.com/css2?family=PT+Serif&display=swap">
<style>
  :root {
    --backdrop: #ffffff;
    --gold-name: #d2ad3c;
    --gold-mark: #a98745;
  }
  html, body {
    margin: 0;
    padding: 0;
    width: 1200px;
    height: 960px;
    overflow: hidden;
    background: var(--backdrop);
  }
  .backdrop {
    position: relative;
    width: 1200px;
    height: 960px;
    background: var(--backdrop);
    font-family: "PT Serif", Georgia, serif;
    font-weight: 400;
  }
  .tile {
    position: absolute;
    transform: translate(-50%, -50%);
    white-space: nowrap;
    line-height: 1;
  }
  .couple-name {
    color: var(--gold-name);
    font-size: 21px;
    letter-spacing: 0.2px;
  }
  .monogram {
    color: var(--gold-mark);
    font-size: 40px;
  }
  .monogram-feature {
    position: absolute;
    left: 597px;
    top: 292px;
    transform: translate(-50%, -50%);
    color: var(--gold-mark);
    font-size: 150px;
    line-height: 1;
    white-space: nowrap;
  }
</style>
</head>
<body>
<main class="backdrop">

  <div class="monogram-feature">C&amp;B</div>

  <!-- row 1 -->
  <div class="tile monogram" style="left:72px;top:75px">C&amp;B</div>
  <div class="tile couple-name" style="left:204px;top:75px">Clara&amp;Bruno</div>
  <div class="tile monogram" style="left:336px;top:75px">C&amp;B</div>
  <div class="tile monogram" style="left:862px;top:75px">C&amp;B</div>
  <div class="tile couple-name" style="left:994px;top:75px">Clara&amp;Bruno</div>
  <div class="tile monogram" style="left:1126px;top:75px">C&amp;B</div>

  <!-- row 2 -->
  <div class="tile couple-name" style="left:72px;top:236px">Clara&amp;Bruno</div>
  <div class="tile monogram" style="left:204px;top:236px">C&amp;B</div>
  <div class="tile monogram" style="left:994px;top:236px">C&amp;B</div>
  <div class="tile couple-name" style="left:1126px;top:236px">Clara&amp;Bruno</div>

  <!-- row 3 -->
  <div class="tile monogram" style="left:72px;top:397px">C&amp;B</div>
  <div class="tile couple-name" style="left:204px;top:397px">Clara&amp;Bruno</div>
  <div class="tile couple-name" style="left:994px;top:397px">Clara&amp;Bruno</div>
  <div class="tile monogram" style="left:1126px;top:397px">C&amp;B</div>

  <!-- row 4 -->
  <div class="tile couple-name" style="left:72px;top:558px">Clara&amp;Bruno</div>
  <div class="tile monogram" style="left:204px;top:558px">C&amp;B</div>
  <div class="tile couple-name" style="left:336px;top:558px">Clara&amp;Bruno</div>
  <div class="tile monogram" style="left:467px;top:558px">C&amp;B</div>
  <div class="tile couple-name" style="left:599px;top:558px">Clara&amp;Bruno</div>
  <div class="tile monogram" style="left:731px;top:558px">C&amp;B</div>
  <div class="tile couple-name" style="left:862px;top:558px">Clara&amp;Bruno</div>
  <div class="tile monogram" style="left:994px;top:558px">C&amp;B</div>
  <div class="tile couple-name" style="left:1126px;top:558px">Clara&amp;Bruno</div>

  <!-- row 5 -->
  <div class="tile monogram" style="left:72px;top:720px">C&amp;B</div>
  <div class="tile couple-name" style="left:204px;top:720px">Clara&amp;Bruno</div>
  <div class="tile monogram" style="left:336px;top:720px">C&amp;B</div>
  <div class="tile couple-name" style="left:467px;top:720px">Clara&amp;Bruno</div>
  <div class="tile monogram" style="left:599px;top:720px">C&amp;B</div>
  <div class="tile couple-name" style="left:731px;top:720px">Clara&amp;Bruno</div>
  <div class="tile monogram" style="left:862px;top:720px">C&amp;B</div>
  <div class="tile couple-name" style="left:994px;top:720px">Clara&amp;Bruno</div>
  <div class="tile monogram" style="left:1126px;top:720px">C&amp;B</div>

  <!-- row 6 -->
  <div class="tile couple-name" style="left:72px;top:882px">Clara&amp;Bruno</div>
  <div class="tile monogram" style="left:204px;top:882px">C&amp;B</div>
  <div class="tile couple-name" style="left:336px;top:882px">Clara&amp;Bruno</div>
  <div class="tile monogram" style="left:467px;top:882px">C&amp;B</div>
  <div class="tile couple-name" style="left:599px;top:882px">Clara&amp;Bruno</div>
  <div class="tile monogram" style="left:731px;top:882px">C&amp;B</div>
  <div class="tile couple-name" style="left:862px;top:882px">Clara&amp;Bruno</div>
  <div class="tile monogram" style="left:994px;top:882px">C&amp;B</div>
  <div class="tile couple-name" style="left:1126px;top:882px">Clara&amp;Bruno</div>

</main>
</body>
</html>
```